Vardel Precision New Website Design

We just changed our logo (thank you ArtFolkly) and company name change from Vardel Precision Machining to Vardel Precision Manufacturing. We do CNC Swiss screw machining and multi-axis machines. We make parts for many industries. We make large quantity production parts as well small R&D quantities. You can look at our current (outdated) website: http://www.vardelprecisionmachining.example to see what we do. We would like a WordPress site, including contact form for "request for quote" . We would also like it to be mobile friendly, and the ability to maintain it ourselves after it is finished I have included our new logo and fonts for references. We would like our site to convey the feeling of precision, capability, and trust worthiness with a very modern look. The new website address is www.vardelprec-mfg.example

Font styles to use
Serif
Sans Serif
Other font styles liked:
• fronts included, not sure if they work

Colors

Designer to choose colors to be used in the design.

Requirements
Must have
• Contact Info, request for quote field

```html
<!DOCTYPE html>
<html lang="en">
<head>
<meta charset="utf-8">
<title>Vardel Precision Manufacturing</title>
<link rel="stylesheet" href="https://fonts.googleapis.com/css2?family=Oswald:wght@500;600;700&family=Montserrat:wght@400;500;600;700&display=swap">
<style>
:root{
  --blue:#1f3f8e;
  --ink:#2a2f38;
  --muted:#5a606b;
  --grey-band:#ebebed;
  --slate:#2f3b4d;
  --night:#15191f;
  --bar:#2b313b;
  --white:#ffffff;
  --line:#e4e4e7;
}
*{box-sizing:border-box;margin:0;padding:0}
html,body{width:1200px;height:3163px;overflow:hidden}
body{position:relative;font-family:"Montserrat",sans-serif;color:var(--ink);background:var(--white)}
.abs{position:absolute}
.heading{font-family:"Oswald",sans-serif;font-weight:600;color:var(--blue);text-transform:uppercase;text-align:center;letter-spacing:.5px}

/* nav */
.site-nav{left:0;top:0;width:1200px;height:56px;background:var(--white);box-shadow:0 1px 4px rgba(0,0,0,.08)}
.brand{left:248px;top:10px;display:flex;align-items:center;gap:8px;font-family:"Montserrat",sans-serif;font-weight:700;font-size:17px;color:var(--blue)}
.brand-dot{width:26px;height:26px;border-radius:50%;background:var(--blue)}
.menu{left:474px;top:16px;display:flex;gap:18px;font-size:11px;font-weight:500}
.menu span{padding:5px 10px;color:var(--ink)}
.menu .active{background:var(--ink);color:var(--white);border-radius:2px}
.menu .contact{color:var(--blue)}

/* hero */
.hero{left:0;top:56px;width:1200px;height:497px;background:radial-gradient(ellipse at 62% 40%,#1e6f7a 0%,#0f2e35 25%,#0b0d10 55%,#050607 100%)}
.hero-title{left:248px;top:180px;font-family:"Oswald",sans-serif;font-weight:700;font-size:54px;line-height:58px;color:var(--white);text-transform:uppercase}
.hero-tag{left:248px;top:305px;width:382px;height:50px;background:var(--white);font-family:"Oswald",sans-serif;font-weight:500;font-size:30px;color:var(--blue);text-align:center;line-height:50px}
.hero-sub{left:248px;top:364px;font-family:"Oswald",sans-serif;font-weight:500;font-size:10.5px;color:var(--white);letter-spacing:.2px}
.btn{height:29px;line-height:27px;text-align:center;font-size:10px;font-weight:600;letter-spacing:.6px;text-transform:uppercase;border-radius:3px}
.btn-solid{background:var(--white);color:var(--ink);border:1px solid var(--white)}
.btn-ghost{color:var(--white);border:1px solid var(--white)}
.btn-dark{color:var(--ink);border:1.5px solid var(--ink)}
.dots{display:flex;align-items:center;gap:14px}
.dots i{display:block;width:5px;height:5px;border-radius:50%;background:rgba(255,255,255,.7)}
.dots i.on{width:11px;height:11px;background:none;border:2px solid #8fb2e8}
.dots b{display:block;width:20px;height:1px;background:rgba(255,255,255,.6)}

/* panels */
.panel{top:553px;width:400px;height:259px}
.panel-a{left:0;background:linear-gradient(135deg,#e9e9eb,#d8d8dc)}
.panel-b{left:400px;background:radial-gradient(circle at 50% 45%,#2c3a2c 0%,#0d0f10 60%)}
.panel-c{left:800px;background:linear-gradient(135deg,#eeeeef,#dcdcdf)}
.panel-label{left:120px;top:101px;width:162px;height:57px;border:1.5px solid #555;border-radius:4px;background:rgba(255,255,255,.6);text-align:center;padding-top:10px}
.panel-b .panel-label{background:var(--white);border-color:var(--white)}
.panel-label strong{display:block;font-size:16px;font-weight:500;letter-spacing:1px;color:#333}
.panel-label small{display:block;font-size:11px;color:#666;margin-top:1px}

/* intro */
.intro-title{left:0;top:862px;width:1200px;font-size:38px}
.intro-text{left:268px;top:924px;width:664px;font-size:12px;line-height:15px;text-align:center;color:#333;font-weight:500}
.intro-text p+p{margin-top:15px}

/* industries */
.industries{left:0;top:1071px;width:1200px;height:266px;background:var(--grey-band)}
.industries-title{left:0;top:50px;width:1200px;font-size:36px}
.industry{top:118px;width:110px;text-align:center}
.industry svg{width:52px;height:52px;fill:#3a3f47}
.industry span{display:block;margin-top:8px;font-size:11.5px;font-weight:600;color:var(--blue)}

/* serve */
.serve{left:0;top:1337px;width:1200px;height:327px;background:linear-gradient(90deg,#2c3748 0%,#34435a 60%,#3c4c63 100%)}
.serve-title{left:248px;color:var(--white);font-size:29px;font-weight:500;line-height:32px}
.serve-title small{display:block;font-size:21px;line-height:26px}
.serve-copy{left:248px;width:360px;color:#e4e7ec;font-size:10.5px;line-height:13px}
.serve-copy p+p{margin-top:13px}
.pledge{left:628px;display:flex;align-items:center;gap:22px;color:var(--white);font-size:14.5px;line-height:18px}
.tick{width:34px;height:34px;flex:none}

/* products */
.products-title{left:0;top:1712px;width:1200px;font-size:36px}
.products-sub{left:300px;top:1762px;width:600px;text-align:center;font-size:11px;line-height:14px;font-weight:600;color:#333}
.product{top:1812px;width:118px;height:118px}
.product-shape{width:100%;height:104px;border-radius:50%}
.product-shadow{margin:6px auto 0;width:70%;height:6px;border-radius:50%;background:radial-gradient(ellipse,#bbb,transparent 70%)}

/* quote */
.quote-left{left:0;top:2052px;width:601px;height:397px;background:linear-gradient(160deg,#3b4655,#2f3845)}
.quote-right{left:601px;top:2052px;width:599px;height:397px;background:radial-gradient(ellipse at 80% 50%,#2b3038 0%,#15191f 60%,#0d0f13 100%)}
.quote-big{left:248px;top:2098px;font-family:"Oswald",sans-serif;font-weight:700;font-size:58px;line-height:62px;color:var(--white);text-transform:uppercase}
.quote-big em{font-style:normal;color:#1e2530}
.quote-sub{left:248px;top:2295px;color:var(--white);font-size:15px;font-weight:600}
.field{height:32px;border:1.5px solid var(--white);color:#d8dbe0;font-size:10px;padding:9px 8px}

/* testimonials */
.testimonials{left:0;top:2449px;width:1200px;height:362px;background:radial-gradient(ellipse at 50% 40%,#4a3a28 0%,#2d2419 45%,#15110c 100%)}
.testi-title{left:0;top:52px;width:1200px;font-family:"Oswald",sans-serif;font-weight:600;font-size:34px;line-height:44px;color:var(--white);text-align:center}
.testi-mark{left:0;top:118px;width:1200px;text-align:center;font-family:"Oswald",sans-serif;font-size:60px;line-height:50px;color:var(--white)}
.testi-text{left:370px;top:176px;width:460px;text-align:center;color:var(--white);font-size:11.5px;line-height:15px;font-weight:500}
.testi-name{left:0;top:240px;width:1200px;text-align:center;color:var(--white);font-size:11px;font-weight:700;line-height:15px}

/* find us */
.footer-brand{left:248px;top:2872px}
.find-title{left:248px;top:2932px;font-family:"Oswald",sans-serif;font-weight:600;font-size:40px;color:var(--blue);line-height:48px}
.find-sub{left:248px;top:2980px;font-size:9.5px;color:#444}
.contact-row{left:248px;width:320px;display:flex;align-items:center;gap:10px;font-size:8.5px;line-height:11px;color:#333}
.contact-row svg{width:13px;height:13px;fill:#222;flex:none}
.map{left:584px;top:2872px;width:367px;height:209px;background:linear-gradient(135deg,#eef0f2,#dde3e8);border:1px solid var(--line)}
.legal{left:0;top:3138px;width:1200px;height:25px;background:var(--bar);color:#d9dce1;font-size:9px;padding:7px 0 0 248px}
</style>
</head>
<body>

<header class="abs site-nav">
  <div class="abs brand"><span class="brand-dot"></span>Vardel Precision</div>
  <nav class="abs menu">
    <span class="active">Home</span><span>About Us</span><span>Our work</span><span>Services</span><span>Equipment</span><span>Quality</span><span class="contact">Contact us</span>
  </nav>
</header>

<section class="abs hero" role="img" aria-label="Dark photo of teal-lit machine gears with miniature worker figures"></section>
<h1 class="abs hero-title">From Blueprint<br>To Reality</h1>
<div class="abs hero-tag">Better Than You Expected</div>
<p class="abs hero-sub">Specializing in precision, Vardel Precision will provide you with superior products, at affordable prices.</p>
<div class="abs btn btn-solid" style="left:248px;top:394px;width:182px">Request a Quote</div>
<div class="abs btn btn-ghost" style="left:441px;top:394px;width:181px">Contact Us</div>
<div class="abs dots" style="left:556px;top:508px"><i></i><b></b><i class="on"></i><b></b><i></i></div>

<section class="abs panel panel-a" role="img" aria-label="Soft grey photo of machined gear parts">
  <div class="abs panel-label"><strong>WHY US</strong><small>Our Mission</small></div>
</section>
<section class="abs panel panel-b" role="img" aria-label="Dark photo of glowing machined components">
  <div class="abs panel-label"><strong>WHO WE ARE</strong><small>About Us</small></div>
</section>
<section class="abs panel panel-c" role="img" aria-label="Soft grey photo of precision gears">
  <div class="abs panel-label"><strong>WHAT WE DO</strong><small>Services</small></div>
</section>

<h2 class="abs heading intro-title">When Less Is More</h2>
<div class="abs intro-text">
  <p>Vardel Precision Machining Company is a high quality machining resource providing friendly service, fast turnaround times, and engineering expertise, at competitive pricing. With almost 20 years of experience in the industry, Vardel Precision utilizes certified state of the art equipment partnered with top professionals to maximize the value and quality in your product.</p>
  <p>Specializing in precision, Vardel Precision will provide you with superior products, at affordable prices.</p>
</div>

<section class="abs industries">
  <h2 class="abs heading industries-title">Industries Served</h2>
  <div class="abs industry" style="left:225px"><svg viewBox="0 0 24 24"><path d="M21 16v-2l-8-5V3.5a1.5 1.5 0 0 0-3 0V9l-8 5v2l8-2.5V19l-2 1.5V22l3.5-1 3.5 1v-1.5L13 19v-5.5z"/></svg><span>Aerospace</span></div>
  <div class="abs industry" style="left:325px"><svg viewBox="0 0 24 24"><path d="M12 2a2.5 2.5 0 0 0-1 4.8V9H8v2h3v8.9A7 7 0 0 1 5.1 14H7l-3-3-3 3h2a9 9 0 0 0 18 0h2l-3-3-3 3h1.9a7 7 0 0 1-5.9 5.9V11h3V9h-3V6.8A2.5 2.5 0 0 0 12 2zm0 1.5a1 1 0 1 1 0 2 1 1 0 0 1 0-2z"/></svg><span>Marine</span></div>
  <div class="abs industry" style="left:422px"><svg viewBox="0 0 24 24"><path d="M7 2C4 2 3 4.5 3 7c0 3 1.5 5 2 8s1 7 2.5 7S9 17 12 17s3 5 4.5 5S18.5 18 19 15s2-5 2-8c0-2.5-1-5-4-5-2 0-3 1-5 1S9 2 7 2z"/></svg><span>Dental</span></div>
  <div class="abs industry" style="left:527px"><svg viewBox="0 0 24 24"><path d="M9 3h6v3h6v15H3V6h6zm1.5 1.5V6h3V4.5zM10.5 10v3h-3v3h3v3h3v-3h3v-3h-3v-3z"/></svg><span>Medical</span></div>
  <div class="abs industry" style="left:643px"><svg viewBox="0 0 24 24"><path d="M4 5h7l2 5h5V7h2v4l2 1v5h-2a3 3 0 0 0-6 0H10a4 4 0 0 0-8 0V12l2-1zm2 2v4h5l-1.5-4zM6 15a2.5 2.5 0 1 1 0 5 2.5 2.5 0 0 1 0-5zm11 0a2 2 0 1 1 0 4 2 2 0 0 1 0-4z"/></svg><span>Automotive</span></div>
  <div class="abs industry" style="left:755px"><svg viewBox="0 0 24 24"><path d="M9 7h6v2h-1v2h1v2h-1v2h1v2H9v-2h1v-2H9v-2h1V9H9zM11 1h2v4h-2zm0 18h2v4h-2zM1 11h4v2H1zm18 0h4v2h-4zM4.2 5.6l1.4-1.4 2.8 2.8-1.4 1.4zm11.4 11.4 1.4-1.4 2.8 2.8-1.4 1.4zM4.2 18.4l2.8-2.8 1.4 1.4-2.8 2.8zM15.6 7l2.8-2.8 1.4 1.4L17 8.4z"/></svg><span>Electronics</span></div>
  <div class="abs industry" style="left:860px"><svg viewBox="0 0 24 24"><path d="M4 4h16v12H4zm2 2v8h12V6zM1 17h22l-1 3H2z"/></svg><span>Computer</span></div>
</section>

<section class="abs serve" role="img" aria-label="Dark blue tinted photo of a fabrication workshop"></section>
<h2 class="abs serve-title" style="top:1389px">We Serve To Meet<small>Your Fabrication Needs</small></h2>
<div class="abs serve-copy" style="top:1476px">
  <p>Our industrial Manufacturing services, suited to meet the needs of numerous industries, are available for any size production run, from prototypes through large volume.</p>
  <p>Additionally, we are committed to providing service suited to each customer's ideal turnaround time. Our rush services can be performed in a matter of hours, if necessary.</p>
</div>
<div class="abs pledge" style="top:1396px"><svg class="tick" viewBox="0 0 34 34"><rect x="1" y="5" width="28" height="28" fill="#fff"/><path d="M7 18l6 6L31 4" stroke="#1f3f8e" stroke-width="5" fill="none"/></svg><span>We are professional, experienced<br>and dedicated to your satisfaction.</span></div>
<div class="abs pledge" style="top:1483px"><svg class="tick" viewBox="0 0 34 34"><rect x="1" y="5" width="28" height="28" fill="#fff"/><path d="M7 18l6 6L31 4" stroke="#1f3f8e" stroke-width="5" fill="none"/></svg><span>We are proud to offer the highest<br>quality services to clients.</span></div>
<div class="abs pledge" style="top:1565px"><svg class="tick" viewBox="0 0 34 34"><rect x="1" y="5" width="28" height="28" fill="#fff"/><path d="M7 18l6 6L31 4" stroke="#1f3f8e" stroke-width="5" fill="none"/></svg><span>Please contact us with any<br>questions you might have.</span></div>

<h2 class="abs heading products-title">Example of Finished Products</h2>
<p class="abs products-sub">Vardel Precision has provided some of the most innovative results for clients, among many different industries. Below are just some of the quality products we were able to produce</p>
<div class="abs product" style="left:268px" role="img" aria-label="Copper flange part"><div class="product-shape" style="background:radial-gradient(circle at 40% 35%,#e8a27c,#b5623e 70%)"></div><div class="product-shadow"></div></div>
<div class="abs product" style="left:418px" role="img" aria-label="Threaded steel fitting"><div class="product-shape" style="background:radial-gradient(circle at 40% 35%,#e6e6e6,#8a8c90 70%)"></div><div class="product-shadow"></div></div>
<div class="abs product" style="left:546px" role="img" aria-label="Machined steel cap"><div class="product-shape" style="background:radial-gradient(circle at 40% 35%,#f0f0f0,#9a9ca0 70%)"></div><div class="product-shadow"></div></div>
<div class="abs product" style="left:673px" role="img" aria-label="Steel threaded nut"><div class="product-shape" style="background:radial-gradient(circle at 40% 35%,#e2e2e2,#85878b 70%)"></div><div class="product-shadow"></div></div>
<div class="abs product" style="left:812px" role="img" aria-label="Black connector assembly"><div class="product-shape" style="background:radial-gradient(circle at 40% 35%,#7a7c80,#1f2124 70%)"></div><div class="product-shadow"></div></div>
<div class="abs btn btn-dark" style="left:510px;top:1963px;width:182px">View All</div>

<section class="abs quote-left"></section>
<section class="abs quote-right" role="img" aria-label="Dark photo of a CNC machine interior"></section>
<h2 class="abs quote-big">Your <em>Part</em><br>Your Design<br>Your <em>Way</em></h2>
<p class="abs quote-sub">Quality From Inception To Completion</p>
<div class="abs btn btn-ghost" style="left:248px;top:2360px;width:184px">Contact Us</div>
<form class="quote-form">
  <div class="abs field" style="left:660px;top:2111px;width:137px">First Name*</div>
  <div class="abs field" style="left:814px;top:2111px;width:137px">Last Name*</div>
  <div class="abs field" style="left:660px;top:2160px;width:137px">Company</div>
  <div class="abs field" style="left:814px;top:2160px;width:137px">Phone</div>
  <div class="abs field" style="left:660px;top:2208px;width:291px">E-mail*</div>
  <div class="abs field" style="left:660px;top:2255px;width:291px;height:86px">Message*</div>
  <div class="abs btn btn-solid" style="left:768px;top:2360px;width:183px">Request a Quote</div>
</form>

<section class="abs testimonials" role="img" aria-label="Warm dark photo of a machinist at work">
  <h2 class="abs testi-title">TESTIMONIALS</h2>
  <div class="abs testi-mark">&ldquo;</div>
  <p class="abs testi-text">Vardel Precision is a company that we can rely on. We often have to react to customer needs quickly and we know that Vardel Precision will take care of us even at a moment's notice. It's always a pleasure to cooperate with them.</p>
  <p class="abs testi-name">Daniel Whitmore<br>Client</p>
  <div class="abs dots" style="left:551px;top:297px"><b></b><i></i><i class="on"></i><i></i><b></b></div>
</section>

<div class="abs brand footer-brand"><span class="brand-dot"></span>Vardel Precision</div>
<h2 class="abs find-title">HOW TO FIND US</h2>
<p class="abs find-sub">If you are living nearby, come visit us at our comfortable office.</p>
<div class="abs contact-row" style="top:3008px"><svg viewBox="0 0 24 24"><path d="M12 2a7 7 0 0 0-7 7c0 5 7 13 7 13s7-8 7-13a7 7 0 0 0-7-7zm0 9.5A2.5 2.5 0 1 1 12 6.5a2.5 2.5 0 0 1 0 5z"/></svg><span>Vardel Precision Machining 1450 Harbor Crest Rd,<br>San Diego, CA 92121</span></div>
<div class="abs contact-row" style="top:3040px"><svg viewBox="0 0 24 24"><path d="M6.6 10.8a15 15 0 0 0 6.6 6.6l2.2-2.2a1 1 0 0 1 1-.25 11.4 11.4 0 0 0 3.6.6 1 1 0 0 1 1 1V20a1 1 0 0 1-1 1A17 17 0 0 1 3 4a1 1 0 0 1 1-1h3.5a1 1 0 0 1 1 1c0 1.25.2 2.45.6 3.6a1 1 0 0 1-.25 1z"/></svg><span>858-555-0142</span></div>
<div class="abs contact-row" style="top:3066px"><svg viewBox="0 0 24 24"><path d="M6 3h12v5H6zm-3 6h18v8h-3v4H6v-4H3zm5 6v4h8v-4z"/></svg><span>858-555-0143</span></div>
<div class="abs contact-row" style="top:3092px"><svg viewBox="0 0 24 24"><path d="M2 5h20v14H2zm2 2v.5l8 5 8-5V7zm0 3v7h16v-7l-8 5z"/></svg><span>info@vardelprecisionmachining.example</span></div>
<div class="abs map" role="img" aria-label="Street map showing the office location in San Diego"></div>

<footer class="abs legal">© Copy Right 2019 All Right Reserved.</footer>

</body>
</html>
```